Tri-fold Brochure design for Bed & Breakfast

I would like a trifold Brochure for my Bed & Breakfast, The Lodge at Birchwater Cove in Holderness, NH. I would like to put as many photos as possible without looking too busy and have space for me to add verbiage about the amenities we offer. We are family and dog friendly and would like to highlight that unique quality. I would like to showcase the rooms, breakfast, family and dog specific amenities, outdoor areas and the beach. Our website is www.lodgeatbirchwatercove.example

Target Market(s)

Families and people with Dogs

Industry/Entity Type

Hospitality

Font styles to use
Serif

Colors
0054AA
0677BA
7BADD7
CADEEF
E8F1F8

Requirements
Must have
• Our logo, space for multiple photos, appropriate for a Bed & Breakfast

```html
<!DOCTYPE html>
<html lang="en">
<head>
<meta charset="utf-8">
<title>The Lodge at Birchwater Cove – Tri-fold Brochure</title>
<link href="https://fonts.googleapis.com/css2?family=Barlow:wght@400;500;600;700&display=swap" rel="stylesheet">
<style>
:root{
  --navy:#0f2a52;
  --blue:#2f74c0;
  --blue-mid:#0677ba;
  --sky:#7badd7;
  --ice:#cadeef;
  --mist:#e8f1f8;
  --white:#ffffff;
  --page:#eef3f7;
}
*{box-sizing:border-box;margin:0;padding:0}
html,body{width:927px;height:1200px;overflow:hidden}
body{background:var(--page);font-family:"Barlow",Arial,sans-serif;color:var(--navy);position:relative}
.sheet{position:absolute;left:89px;width:749px;height:529px;background:var(--white);overflow:hidden;box-shadow:6px 8px 14px rgba(15,42,82,.18)}
.sheet--outside{top:51px}
.sheet--inside{top:626px}
.abs{position:absolute}
.photo{position:absolute}

/* outside */
.top-rule{left:0;top:0;width:749px;height:17px;background:var(--navy)}
.amenities{left:0;top:17px;width:246px;height:263px;background:var(--navy);color:var(--white)}
.panel-head{height:33px;background:var(--blue);color:var(--white);font-weight:600;font-size:17.5px;letter-spacing:.2px;display:flex;align-items:center;justify-content:center}
.amenities ul{list-style:none;padding:14px 6px 0 20px}
.amenities li{font-size:11.6px;line-height:14px;margin-bottom:18px;padding-left:9px;position:relative}
.amenities li::before{content:"•";position:absolute;left:0}
.packages-head{left:246px;top:17px;width:251px}
.packages-photo{left:246px;top:50px;width:251px;height:230px;background:linear-gradient(160deg,#9db39a,#c7b38a 55%,#9a6a3a)}
.packages{left:256px;top:60px;width:235px;color:var(--white);text-shadow:0 1px 3px rgba(0,0,0,.5)}
.pkg{position:relative;padding-left:26px;margin-bottom:8px}
.pkg svg{position:absolute;left:0;top:3px}
.pkg h3{font-size:14px;font-weight:500;line-height:17px}
.pkg p{font-size:10.5px;line-height:13px}
.contact-head{left:246px;top:280px;width:251px;height:26px;background:var(--blue);color:var(--white);font-weight:600;font-size:17px;display:flex;align-items:center;justify-content:center}
.contact{left:256px;top:316px;width:240px;font-size:11.6px}
.contact dt{font-weight:600;display:flex;align-items:center;gap:3px;margin-bottom:4px}
.contact dd{margin-bottom:14px;line-height:15px}
.socials{left:292px;top:463px;display:flex;gap:18px}
.socials span{width:19px;height:19px;border-radius:50%;background:var(--blue-mid)}
.couple-photo{left:0;top:280px;width:246px;height:215px;background:linear-gradient(180deg,#c9d6de,#7f93a3 45%,#b48a6a 75%,#8a6248)}
.footer-band{height:17px;background:var(--blue);color:var(--white);font-size:9.6px;font-weight:600;letter-spacing:2.4px;display:flex;align-items:center;justify-content:center}
.front-footer{left:246px;top:495px;width:251px}
.cover-top{left:497px;top:11px;width:252px;height:102px;background:linear-gradient(90deg,#c9c4b8,#f3f1ec)}
.logo-seal{left:566px;top:11px;width:102px;height:102px;border-radius:50%;background:var(--white);border:3px solid var(--navy);display:flex;align-items:center;justify-content:center;text-align:center;font-size:12px;font-weight:600;line-height:14px;padding:10px;color:var(--navy)}
.cover-rule{left:497px;top:113px;width:252px;height:12px;background:var(--navy)}
.room-photo{left:497px;top:125px;width:252px;height:251px;background:linear-gradient(170deg,#d8dcdf,#aab0b6 50%,#8a7f94)}
.cover{left:497px;top:376px;width:252px;height:153px;background:var(--navy);color:var(--white);text-align:center;padding-top:8px}
.cover p{font-size:17.5px;line-height:22px}
.cover strong{font-weight:600;font-size:18px}
.cover small{display:block;font-size:11px;line-height:14px;margin-top:4px}
.cover .footer-band{position:absolute;left:0;top:119px;width:252px}

/* inside */
.lawn-photo{left:0;top:0;width:749px;height:189px;background:linear-gradient(180deg,#9fb7c7,#6f9a5e 45%,#a7a296 80%)}
.inside-band{left:0;top:174px;width:749px;height:15px;background:var(--navy)}
.thumb{top:104px;width:98px;height:101px;border:3px solid var(--navy)}
.included{left:30px;top:205px;width:210px}
.included h2{font-size:20px;font-weight:700;margin-bottom:12px;letter-spacing:.2px}
.item{position:relative;padding-left:14px;margin-bottom:9px}
.item svg{position:absolute;left:0;top:2px}
.item h3{font-size:12px;font-weight:500;line-height:14px}
.item p{font-size:12px;line-height:15px}
.included-2{left:258px;top:218px;width:232px}
.story{left:505px;top:189px;width:244px;height:303px;background:linear-gradient(180deg,#4b82c0,#6f9fd0);color:var(--white);padding:12px 14px 0 12px}
.story p{font-size:11.2px;line-height:15.2px;margin-bottom:8px;padding-left:7px;position:relative}
.story p::before{content:"•";position:absolute;left:0}
.inside-footer{left:0;top:492px;width:749px;justify-content:flex-start;padding-left:36px}
.inside-base{left:0;top:509px;width:749px;height:20px;background:var(--navy)}
</style>
</head>
<body>

<section class="sheet sheet--outside">
  <div class="abs top-rule"></div>

  <div class="abs amenities">
    <h2 class="panel-head">OUR DOG AMENITIES</h2>
    <ul>
      <li>Doggie breakfast menu</li>
      <li>1/4 acre on-site fully fenced dog park</li>
      <li>Private beach for dogs to swim nearby</li>
      <li>On-site hiking trails and scenic public hiking trails minutes away</li>
      <li>Dog sitting available for dinner dates</li>
      <li>6 dog friendly rooms</li>
    </ul>
  </div>
  <div class="photo couple-photo" role="img" aria-label="Couple with their dogs on a rocky summit overlooking the lake"></div>

  <h2 class="abs panel-head packages-head">SPECIAL PACKAGES</h2>
  <div class="photo packages-photo" role="img" aria-label="Sunlit dining room with wooden tables and fireplace"></div>
  <div class="abs packages">
    <div class="pkg"><svg width="11" height="16" viewBox="0 0 11 16"><path d="M0 0h11v16l-5.5-4L0 16z" fill="#fff"/></svg><h3>Anniversary Package</h3><p>Available Year-Round<br>Stay for at least 1 night</p></div>
    <div class="pkg"><svg width="11" height="16" viewBox="0 0 11 16"><path d="M0 0h11v16l-5.5-4L0 16z" fill="#fff"/></svg><h3>Basket Making at the Lodge</h3><p>Available Year-Round</p></div>
    <div class="pkg"><svg width="11" height="16" viewBox="0 0 11 16"><path d="M0 0h11v16l-5.5-4L0 16z" fill="#fff"/></svg><h3>Birthday Special</h3><p>Available November-May<br>Stay for at least 1 night</p></div>
    <div class="pkg"><svg width="11" height="16" viewBox="0 0 11 16"><path d="M0 0h11v16l-5.5-4L0 16z" fill="#fff"/></svg><h3>Stay &amp; Dine</h3><p>Available November-May<br>Stay for at least 1 night</p></div>
  </div>

  <h2 class="abs contact-head">Contact US</h2>
  <dl class="abs contact">
    <dt><svg width="11" height="11" viewBox="0 0 12 12"><circle cx="6" cy="6" r="6" fill="#0f2a52"/><path d="M4 3.2l1.2 1.4-.6.8c.4.8 1 1.4 1.8 1.8l.8-.6 1.4 1.2-.7 1c-2.4-.3-4.4-2.3-4.7-4.7z" fill="#fff"/></svg>PHONE</dt>
    <dd>603.555.0142</dd>
    <dt><svg width="11" height="9" viewBox="0 0 12 9"><rect width="12" height="9" rx="1" fill="#0f2a52"/><path d="M1 1l5 4 5-4" stroke="#fff" fill="none"/></svg>EMAIL</dt>
    <dd style="font-size:10.4px">innkeepers@lodgeatbirchwatercove.example</dd>
    <dt><svg width="9" height="12" viewBox="0 0 9 12"><path d="M4.5 0A4.5 4.5 0 0 0 0 4.5C0 8 4.5 12 4.5 12S9 8 9 4.5A4.5 4.5 0 0 0 4.5 0z" fill="#0f2a52"/><circle cx="4.5" cy="4.5" r="1.6" fill="#fff"/></svg>ADDRESS</dt>
    <dd>214 Birch Hollow Road<br>Holderness, New Hampshire 03245 US</dd>
  </dl>
  <div class="abs socials" aria-label="Social media links"><span></span><span></span><span></span><span></span></div>
  <div class="abs footer-band front-footer">www.lodgeatbirchwatercove.example</div>

  <div class="photo cover-top" role="img" aria-label="Bedside table with flowers and breakfast tray on white linens"></div>
  <div class="abs logo-seal">The Lodge at Birchwater Cove</div>
  <div class="abs cover-rule"></div>
  <div class="photo room-photo" role="img" aria-label="Bright guest room with upholstered bed and lavender throw"></div>
  <div class="abs cover">
    <p>A top-rated<br><strong>FAMILY &amp; DOG FRIENDLY</strong><br>Bed &amp; Breakfast</p>
    <small>near Squam Lake in Holderness,<br>New Hampshire</small>
    <div class="footer-band">www.lodgeatbirchwatercove.example</div>
  </div>
</section>

<section class="sheet sheet--inside">
  <div class="photo lawn-photo" role="img" aria-label="Stone patio with umbrella tables overlooking green lawn and trees"></div>
  <div class="abs inside-band"></div>
  <div class="photo thumb" style="left:28px;background:linear-gradient(#e6e8ea,#b9bec4)" role="img" aria-label="Guest room with white bedding"></div>
  <div class="photo thumb" style="left:138px;background:linear-gradient(#c9ccc4,#7d8a5a)" role="img" aria-label="Patio with fire pit and flowers"></div>
  <div class="photo thumb" style="left:267px;background:linear-gradient(#c89a5a,#8a5a2a)" role="img" aria-label="French toast breakfast"></div>
  <div class="photo thumb" style="left:378px;background:linear-gradient(#d7c4a8,#b23a3a 60%,#3a3f7a)" role="img" aria-label="Pancakes with fresh berries"></div>
  <div class="photo thumb" style="left:513px;background:linear-gradient(#7aa0c8,#4f7a3a 45%,#3a5a7a)" role="img" aria-label="Guest on a dock beside a wooden boat"></div>
  <div class="photo thumb" style="left:624px;background:linear-gradient(#9cbad8,#3a7ab0)" role="img" aria-label="Kayaking on the lake"></div>

  <div class="abs included">
    <h2>WHAT IS INCLUDED</h2>
    <div class="item"><svg width="9" height="12" viewBox="0 0 9 12"><path d="M0 0h9v12l-4.5-3L0 12z" fill="#0f2a52"/></svg><h3>SPACIOUS ROOMS</h3><p>Well-appointed accommodations with full private bath, A/C, luxury linens, Wi-Fi, Smart TV, BrewMate</p></div>
    <div class="item"><svg width="9" height="12" viewBox="0 0 9 12"><path d="M0 0h9v12l-4.5-3L0 12z" fill="#0f2a52"/></svg><h3>DELICIOUS BREAKFAST</h3><p>Delicious cooked to order breakfast daily. Made with eggs from the coop and pork from our pigs. Breakfast in ed is always an option!</p></div>
    <div class="item"><svg width="9" height="12" viewBox="0 0 9 12"><path d="M0 0h9v12l-4.5-3L0 12z" fill="#0f2a52"/></svg><h3>DOG WELCOME</h3><p>1/4 acre fully enclosed dog park, dog friendly hiking trails and a special doggie breakfast menu!</p></div>
  </div>

  <div class="abs included-2">
    <div class="item"><svg width="9" height="12" viewBox="0 0 9 12"><path d="M0 0h9v12l-4.5-3L0 12z" fill="#0f2a52"/></svg><h3>LAKE ACCESS</h3><p>Complimentary kayaking, stand up paddle boarding &amp; swimming at a private beach just a short walk away. Beach towels &amp; all equipment provided.</p></div>
    <div class="item"><svg width="9" height="12" viewBox="0 0 9 12"><path d="M0 0h9v12l-4.5-3L0 12z" fill="#0f2a52"/></svg><h3>FAMILY ENTERTAINMENT</h3><p>Complimentary s'mores, arts &amp; crafts and Parent Date Night- the kids eat pizza &amp; watch a movie with us while you enjoy alone time together!</p></div>
    <div class="item"><svg width="9" height="12" viewBox="0 0 9 12"><path d="M0 0h9v12l-4.5-3L0 12z" fill="#0f2a52"/></svg><h3>OUTDOOR FUN</h3><p>7+ acres of beautiful grounds, patio with 2 fire pits, farm animals, outdoor play set &amp; sandbox, on-site &amp; nearby hiking trails with amazing lake views.</p></div>
  </div>

  <div class="abs story">
    <p>We are a high-end, upscale B&amp;B that offers complimentary family &amp; dog friendly amenities &amp; activities to ensure guests and their families have a stress free, fun-filled and memorable vacation experience together.</p>
    <p>Having 3 young children and 2 rescue pups, we understand the challenges of finding family-oriented, pet friendly lodging with upscale amenities.</p>
    <p>Between the beautiful historic Lodge with rustic chic decor and modern amenities, expansive grounds, family fun activities, a menagerie of farm animals and access to beautiful Squam Lake, there truly is something for everyone to enjoy!!</p>
  </div>

  <div class="abs footer-band inside-footer">www.lodgeatbirchwatercove.example</div>
  <div class="abs inside-base"></div>
</section>

</body>
</html>
```